Step Lantern - a dance school theatre production

We need a visually eye catching poster design which advertises our forthcoming theatre production "Step Lantern" Sized A2

Our dance school is professional yet funky and modern, and we wish to portray this visually.

This has to be vibrant and colourful, with the school name and production name being the initial eye catching theme.

Our dance school name is the Holloway-Brent School of Dance

Our dance school offers a variety of dance styles including ballet,tap,street, jazz,rock and roll

Requirements
Must have
• "Step Lantern" as the production name
www.hbschoolofdance.example.co.uk
Marlow Grange Theatre 01632 960417
30th September 2011-1st October 2011
price; £8 adults , £7 concessions
tickets available from the theatre box office
Nice to have
• an eye catching main image incorporated into the design?
Should not have
• no flowery fonts please

```html
<!DOCTYPE html>
<html lang="en">
<head>
<meta charset="utf-8">
<title>Step Lantern – Holloway-Brent School of Dance</title>
<link rel="stylesheet" href="https://fonts.googleapis.com/css2?family=EB+Garamond:ital,wght@0,500;1,400;1,700&family=Rye&display=swap">
<style>
  :root {
    --red: #e8262b;
    --orange: #f26a1e;
    --amber: #f8a51c;
    --yellow: #fcd531;
    --purple: #8a3f98;
    --purple-deep: #6b2c82;
    --cream: #fff6e0;
    --dancer: rgba(255, 214, 140, 0.92);
    --dancer-faint: rgba(255, 200, 150, 0.32);
    --white: #ffffff;
  }
  * { margin: 0; padding: 0; box-sizing: border-box; }
  html, body { width: 845px; height: 1200px; overflow: hidden; }
  body { background: var(--white); }

  .poster {
    position: relative;
    width: 845px;
    height: 1200px;
    overflow: hidden;
    background: radial-gradient(ellipse 120% 95% at 50% 88%, var(--yellow) 0%, var(--amber) 30%, var(--orange) 58%, var(--red) 88%);
    font-family: "EB Garamond", Georgia, serif;
    font-style: italic;
    text-align: center;
  }

  .rays { position: absolute; inset: 0; }

  .music-notes, .dancer {
    position: absolute;
  }
  .music-notes {
    background: radial-gradient(ellipse at center, var(--dancer-faint) 0%, rgba(255,200,150,0.12) 55%, transparent 75%);
    border-radius: 50%;
  }
  .notes-left  { left: -60px; top: 330px; width: 260px; height: 420px; }
  .notes-right { right: -70px; top: 300px; width: 280px; height: 460px; }
  .notes-top   { left: 300px; top: -40px; width: 300px; height: 180px; }
  .notes-low   { left: 180px; top: 780px; width: 480px; height: 200px; opacity: .7; }

  .dancer {
    background: radial-gradient(ellipse at 50% 45%, var(--dancer) 0%, var(--dancer) 45%, rgba(255,214,140,0.35) 70%, transparent 78%);
    border-radius: 46% 54% 50% 50%;
  }
  .dancer-ballet-leap   { left: 40px;  top: 32px;  width: 115px; height: 140px; }
  .dancer-tumble        { left: 142px; top: 146px; width: 105px; height: 108px; }
  .dancer-ballerina     { left: 608px; top: 166px; width: 118px; height: 106px; }
  .dancer-faint-top     { left: 432px; top: 48px;  width: 92px;  height: 92px; opacity: .45; }
  .dancer-breakdance    { left: 80px;  top: 735px; width: 100px; height: 168px; }
  .dancer-jazz          { left: 684px; top: 676px; width: 115px; height: 160px; }

  .date-ribbon {
    position: absolute;
    top: 42px;
    right: -70px;
    width: 340px;
    height: 78px;
    background: var(--purple);
    color: var(--white);
    transform: rotate(36deg);
    font-style: normal;
    font-weight: 500;
    font-size: 23px;
    line-height: 26px;
    padding-top: 13px;
  }

  .presenter {
    position: absolute;
    top: 112px;
    left: 0; right: 0;
    color: var(--cream);
    font-weight: 700;
    font-size: 42px;
    line-height: 50px;
  }

  .title {
    position: absolute;
    top: 318px;
    left: 0; right: 0;
    font-family: "Rye", "Times New Roman", serif;
    font-style: normal;
    font-weight: 400;
    color: var(--white);
    text-shadow: -8px 6px 0 var(--purple-deep);
    line-height: 1;
  }
  .title span { display: block; }
  .title .word-one { font-size: 172px; letter-spacing: 18px; padding-left: 18px; }
  .title .word-two { font-size: 124px; margin-top: 34px; }

  .venue {
    position: absolute;
    top: 748px;
    left: 0; right: 0;
    color: var(--cream);
    font-weight: 700;
    font-size: 42px;
    line-height: 56px;
  }

  .tickets {
    position: absolute;
    top: 930px;
    left: 0; right: 0;
    color: var(--purple);
    font-weight: 700;
    font-size: 31px;
    line-height: 48px;
  }

  .info-band {
    position: absolute;
    top: 1052px;
    left: 0; right: 0;
    height: 118px;
    background: var(--purple);
    color: var(--white);
    font-size: 29px;
    line-height: 42px;
    padding-top: 16px;
  }
</style>
</head>
<body>
<main class="poster">
  <svg class="rays" width="845" height="1200" viewBox="0 0 845 1200" aria-hidden="true">
    <g stroke="#ffe66b" stroke-width="1.2" opacity="0.8">
      <line x1="422" y1="1050" x2="0" y2="0"/>
      <line x1="422" y1="1050" x2="90" y2="0"/>
      <line x1="422" y1="1050" x2="180" y2="0"/>
      <line x1="422" y1="1050" x2="260" y2="0"/>
      <line x1="422" y1="1050" x2="330" y2="0"/>
      <line x1="422" y1="1050" x2="395" y2="0"/>
      <line x1="422" y1="1050" x2="455" y2="0"/>
      <line x1="422" y1="1050" x2="515" y2="0"/>
      <line x1="422" y1="1050" x2="585" y2="0"/>
      <line x1="422" y1="1050" x2="660" y2="0"/>
      <line x1="422" y1="1050" x2="745" y2="0"/>
      <line x1="422" y1="1050" x2="845" y2="0"/>
      <line x1="422" y1="1050" x2="845" y2="140"/>
      <line x1="422" y1="1050" x2="845" y2="320"/>
      <line x1="422" y1="1050" x2="845" y2="520"/>
      <line x1="422" y1="1050" x2="845" y2="740"/>
      <line x1="422" y1="1050" x2="0" y2="140"/>
      <line x1="422" y1="1050" x2="0" y2="320"/>
      <line x1="422" y1="1050" x2="0" y2="520"/>
      <line x1="422" y1="1050" x2="0" y2="740"/>
    </g>
  </svg>

  <div class="music-notes notes-left" role="img" aria-label="Faint swirling music notes"></div>
  <div class="music-notes notes-right" role="img" aria-label="Faint swirling music notes"></div>
  <div class="music-notes notes-top" role="img" aria-label="Faint music notes and a pale dancing couple"></div>
  <div class="music-notes notes-low" role="img" aria-label="Faint music notes"></div>

  <div class="dancer dancer-ballet-leap" role="img" aria-label="Pale silhouette of a ballet dancer in a high kick"></div>
  <div class="dancer dancer-tumble" role="img" aria-label="Pale silhouette of a dancer in a back flip"></div>
  <div class="dancer dancer-ballerina" role="img" aria-label="Pale silhouette of a ballerina in a tutu"></div>
  <div class="dancer dancer-faint-top" role="img" aria-label="Faint silhouette of a ballet dancer"></div>
  <div class="dancer dancer-breakdance" role="img" aria-label="Pale silhouette of a street dancer in a hand freeze"></div>
  <div class="dancer dancer-jazz" role="img" aria-label="Pale silhouette of a jazz dancer with arms raised"></div>

  <div class="date-ribbon">30th September<br>- 1st October 2011</div>

  <header class="presenter">Holloway-Brent<br>School of Dance<br>presents</header>

  <h1 class="title"><span class="word-one">STEP</span><span class="word-two">LANTERN</span></h1>

  <p class="venue">at Marlow Grange<br>Theatre</p>

  <p class="tickets">Tickets available from the theatre box office<br>£8 adults, £7 concessions</p>

  <footer class="info-band">For more information call 01632 960417<br>or visit www.hbschoolofdance.example.co.uk</footer>
</main>
</body>
</html>
```